Veltrona stationery design

Design stationery for us that fits with the colours of the logo. We are looking for letterheads, business cards etc. Something we can use for a prospectus and marketing presentations in power point. Must be completed in such a manner that it represents a corporate image for large enterprise clients and other large organisations. The company is a project assurance and monitoring company that works in all industries.

```html
<!DOCTYPE html>
<html lang="en">
<head>
<meta charset="utf-8">
<title>Veltrona stationery</title>
<link rel="stylesheet" href="https://fonts.googleapis.com/css2?family=Inter:wght@500;600;700;800&family=Jost:wght@400;500&display=swap">
<style>
:root{
  --bg:#48494b;
  --paper:#ffffff;
  --navy:#1b2d63;
  --navy-deep:#0f2146;
  --blue:#2d5aa8;
  --sky:#2ea6dd;
  --orange:#f7931e;
  --red:#e31e24;
  --ink:#1a1a1a;
}
*{margin:0;padding:0;box-sizing:border-box}
html,body{width:1200px;height:1200px;overflow:hidden;background:var(--bg)}
body{position:relative;font-family:"Jost",sans-serif;color:var(--ink)}
.sheet{position:absolute;overflow:hidden}
.sheet svg.art{position:absolute;inset:0;width:100%;height:100%}
.brand{position:absolute;display:flex;align-items:center;gap:7px;font-family:"Inter",sans-serif;font-weight:800;color:var(--navy);letter-spacing:.02em}
.brand .dot{border-radius:50%;background:var(--navy)}
.brand.light{color:#ffffff}
.brand.light .dot{background:#ffffff}

/* letterhead */
.letterhead{left:41px;top:174px;width:682px;height:882px;background:var(--paper)}
.letterhead .brand{left:92px;top:126px;font-size:28px}
.letterhead .brand .dot{width:26px;height:26px}
.tagline{position:absolute;left:94px;top:279px;font-family:"Inter",sans-serif;font-weight:600;font-size:15px;line-height:19px}
.tagline .primary{color:var(--navy)}
.tagline .accent{color:var(--red)}
.letter-body{position:absolute;left:94px;top:347px;width:442px;font-family:"Inter",sans-serif;font-size:10.3px;line-height:19px;color:#2a2a2a}
.signoff{position:absolute;left:94px;top:529px;font-family:"Inter",sans-serif}
.signoff .close{font-weight:600;font-size:14.5px}
.signoff .name{font-weight:600;font-size:14.5px;margin-top:6px;margin-left:2px}
.signoff .role{font-family:"Jost",sans-serif;font-size:9.5px;margin-top:2px;margin-left:2px}
.footer-rule{position:absolute;left:94px;top:765px;width:338px;height:1px;background:#8a8a8a}
.footer-contact{position:absolute;top:780px;font-size:9.5px;line-height:11.7px}
.footer-contact.phone{left:97px}
.footer-contact.address{left:216px;top:782px}

/* envelope */
.envelope{left:766px;top:175px;width:388px;height:221px;background:linear-gradient(160deg,#2f5aa6 0%,#223f82 45%,#1b2d63 100%)}
.envelope .brand{left:120px;top:43px;font-size:16px}
.envelope .brand .dot{width:15px;height:15px}

/* card front */
.card-front{left:771px;top:425px;width:388px;height:221px;background:var(--paper)}
.card-front .brand{left:49px;top:52px;font-size:20px}
.card-front .brand .dot{width:18px;height:18px}
.card-contact{position:absolute;left:57px;top:128px;font-size:11.5px;line-height:14.5px}

/* dark card */
.card-dark{left:821px;top:700px;width:276px;height:157px;border-radius:8px;background:linear-gradient(160deg,#2c519c 0%,#14275a 45%,#0f2146 100%)}
.card-dark .brand{left:64px;top:66px;font-size:16px}
.card-dark .brand .dot{width:14px;height:14px}

/* card back */
.card-back{left:821px;top:895px;width:276px;height:157px;border-radius:8px;background:var(--paper)}
.card-back .brand{left:32px;top:80px;font-size:13px;flex-direction:column;gap:5px}
.card-back .brand .dot{width:18px;height:18px}
.card-back .divider{position:absolute;left:140px;top:33px;width:1px;height:87px;background:#666}
.card-person{position:absolute;left:160px;top:34px;font-size:6.4px;line-height:8px}
.card-person .name{font-family:"Inter",sans-serif;font-weight:600;font-size:12.5px;line-height:14px}
.card-person .gap{height:7px}
</style>
</head>
<body>

<svg width="0" height="0" style="position:absolute" aria-hidden="true">
  <defs>
    <linearGradient id="accent-warm" x1="0" y1="0" x2="1" y2="1">
      <stop offset="0" stop-color="#2d5aa8"/><stop offset=".55" stop-color="#2ea6dd"/><stop offset="1" stop-color="#f7931e"/>
    </linearGradient>
    <linearGradient id="accent-cool" x1="0" y1="0" x2="1" y2="1">
      <stop offset="0" stop-color="#2d5aa8"/><stop offset="1" stop-color="#1b2d63"/>
    </linearGradient>
  </defs>
</svg>

<section class="sheet letterhead">
  <svg class="art" viewBox="0 0 682 882" preserveAspectRatio="none" role="img" aria-label="Decorative corner accent area in brand blue and orange tones">
    <path d="M500 0 L682 0 L682 190 Z" fill="url(#accent-cool)"/>
    <path d="M682 620 L682 882 L440 882 Z" fill="url(#accent-warm)"/>
  </svg>

  <div class="brand"><span class="dot"></span>VELTRONA</div>

  <div class="tagline">
    <div class="primary">Project Assurance</div>
    <div class="accent">Performance Delivered</div>
  </div>

  <p class="letter-body">Veltrona provides independent assurance across the full life of a project, from early planning through to final handover. Our reviewers work alongside sponsors and delivery teams to test schedules, budgets and risks against agreed goals, giving boards a clear and timely view of progress. We have supported programmes in energy, transport, health and public services, helping leaders spot issues early and act with confidence. Each engagement is shaped to the needs of the client, and every report is written to be read, understood and used to keep performance on track across the whole portfolio.</p>

  <div class="signoff">
    <div class="close">Sincerely</div>
    <div class="name">John Doe</div>
    <div class="role">Chief Executive Officer</div>
  </div>

  <div class="footer-rule"></div>
  <div class="footer-contact phone">+61 2 5550 0142<br>john.doe@veltrona<br>www.veltrona.com</div>
  <div class="footer-contact address">Level 9, 48 Harbour Lane<br>Sydney NSW 2000<br>Australia</div>
</section>

<section class="sheet envelope">
  <svg class="art" viewBox="0 0 388 221" preserveAspectRatio="none" role="img" aria-label="Envelope flap and corner accent in brand tones">
    <path d="M0 0 L388 0 L352 82 Q346 95 332 95 L56 95 Q42 95 37 82 Z" fill="#2a52a0"/>
    <path d="M0 0 L37 82 Q42 95 56 95 L332 95 Q346 95 352 82 L388 0" fill="none" stroke="#152a5c" stroke-opacity=".45" stroke-width="1.5"/>
    <path d="M388 150 L388 221 L290 221 Z" fill="url(#accent-warm)"/>
  </svg>
  <div class="brand light"><span class="dot"></span>VELTRONA</div>
</section>

<section class="sheet card-front">
  <svg class="art" viewBox="0 0 388 221" preserveAspectRatio="none" role="img" aria-label="Corner accent in brand tones">
    <path d="M388 150 L388 221 L290 221 Z" fill="url(#accent-warm)"/>
  </svg>
  <div class="brand"><span class="dot"></span>VELTRONA</div>
  <div class="card-contact">+61 2 5550 0142<br>john.doe@veltrona<br>www.veltrona.com</div>
</section>

<section class="sheet card-dark">
  <svg class="art" viewBox="0 0 276 157" preserveAspectRatio="none" role="img" aria-label="Corner accent in brand tones">
    <path d="M276 100 L276 157 L190 157 Z" fill="url(#accent-warm)"/>
  </svg>
  <div class="brand light"><span class="dot"></span>VELTRONA</div>
</section>

<section class="sheet card-back">
  <svg class="art" viewBox="0 0 276 157" preserveAspectRatio="none" role="img" aria-label="Corner accent in brand tones">
    <path d="M276 110 L276 157 L200 157 Z" fill="url(#accent-warm)"/>
  </svg>
  <div class="brand"><span class="dot"></span>VELTRONA</div>
  <div class="divider"></div>
  <div class="card-person">
    <div class="name">John Doe</div>
    <div>Chief Executive Officer</div>
    <div class="gap"></div>
    <div>+61 2 5550 0142<br>john.doe@veltrona<br>www.veltrona.com</div>
    <div class="gap"></div>
    <div>Level 9, 48 Harbour Lane<br>Sydney NSW 2000<br>Australia</div>
  </div>
</section>

</body>
</html>
```